Business Card Trio Design

We need a set of business cards that all match but are not identical. We need one generic for the business and one for each of the two owners. We would like the cards to be similar to each other, but not identical. We have a logo and the colors of the logo are painstakingly chosen so if blue or green is used, we prefer our specific blue and green. Our logo pops better on a black background as well. We are open to double-sided, but it is not the top choice. We would love some either gold or silver accents that are in a foiled appearance. We sell uniforms (scrubs, culinary, EMT, police, fire, business, all types except kids and sports), shoes, equipment, and accessories. We also have facebook, pinterest, instagram, and twitter that we would like to have them follow and we offer splitwell in the store we would like the card to also advertise.

```html
<!DOCTYPE html>
<html lang="en">
<head>
<meta charset="utf-8">
<title>Verdant Workwear – Business Card</title>
<link href="https://fonts.googleapis.com/css2?family=Montserrat:wght@400;500;600;700&display=swap" rel="stylesheet">
<style>
  :root{
    --stage:#3a3330;
    --card:#1f1f20;
    --card-back:#151516;
    --brand-blue:#8fb0cf;
    --brand-green:#12a383;
    --ink:#ffffff;
    --ink-soft:#d9d9d9;
    --emboss:#262628;
  }
  *{margin:0;padding:0;box-sizing:border-box}
  html,body{width:1200px;height:786px;overflow:hidden;background:var(--stage);font-family:"Montserrat",sans-serif}
  .canvas{position:relative;width:1200px;height:786px}
  .card{position:absolute;width:540px;height:309px;border-radius:4px;overflow:hidden;box-shadow:0 14px 30px rgba(0,0,0,.45)}
  .card--front{left:40px;top:240px;background:var(--card)}
  .card--back{left:620px;top:240px;background:var(--card-back)}

  .brand{position:absolute;left:40px;top:42px;display:flex;align-items:center;gap:16px}
  .brand__dot{width:62px;height:62px;border-radius:50%;background:var(--brand-green)}
  .brand__name{font-weight:600;font-size:30px;letter-spacing:3px;line-height:1.05;color:var(--brand-blue);text-transform:uppercase}

  .divider{position:absolute;left:40px;right:30px;top:168px;height:1.5px;background:var(--brand-green)}

  .person{position:absolute;left:40px;top:130px}
  .person__name{font-weight:700;font-size:21px;color:var(--brand-green)}
  .person__role{font-size:12px;color:var(--ink);margin-top:1px}

  .contacts{position:absolute;left:40px;top:180px;list-style:none}
  .contacts li{display:flex;align-items:center;gap:9px;font-size:12.5px;color:var(--ink);height:19px}
  .contacts svg{width:11px;height:11px;fill:var(--brand-green)}

  .address{position:absolute;right:30px;top:122px;text-align:right;font-size:12px;line-height:1.3;color:var(--ink)}
  .address__company{color:var(--brand-green);font-size:13px}

  .bands{position:absolute;left:0;bottom:0;width:540px;height:120px}

  .back-mark{position:absolute;left:90px;top:44px;width:220px;height:220px;border-radius:50%;background:var(--emboss);box-shadow:inset 0 2px 6px rgba(255,255,255,.06),inset 0 -4px 10px rgba(0,0,0,.6)}
  .back-name{position:absolute;right:36px;top:132px;font-weight:600;font-size:20px;letter-spacing:2.5px;line-height:1.1;color:var(--brand-blue);text-transform:uppercase;text-align:left}
</style>
</head>
<body>
<main class="canvas">

  <section class="card card--front" aria-label="Business card front">
    <div class="brand">
      <span class="brand__dot"></span>
      <span class="brand__name">Verdant<br>Workwear</span>
    </div>

    <div class="address">
      <div class="address__company">Verdant Workwear</div>
      <div>418 Harbor Row</div>
      <div>Fairmont, NC 27091</div>
    </div>

    <div class="person">
      <div class="person__name">Marcus Delane</div>
      <div class="person__role">Owner</div>
    </div>

    <div class="divider"></div>

    <ul class="contacts">
      <li><svg viewBox="0 0 16 16"><path d="M3 1h3l1.5 4-2 1.5a9 9 0 0 0 4 4L11 8.5l4 1.5v3a2 2 0 0 1-2 2C7 15 1 9 1 3a2 2 0 0 1 2-2z"/></svg>(555) 214-6630</li>
      <li><svg viewBox="0 0 16 16"><path d="M3 1h3l1.5 4-2 1.5a9 9 0 0 0 4 4L11 8.5l4 1.5v3a2 2 0 0 1-2 2C7 15 1 9 1 3a2 2 0 0 1 2-2z"/></svg>(555) 381-0457</li>
      <li><svg viewBox="0 0 16 16"><path d="M1 3h14v10H1z M1 3l7 6 7-6" fill="none" stroke="#12a383" stroke-width="2"/></svg>verdantworkwearshop@mailbox.com</li>
      <li><svg viewBox="0 0 16 16"><circle cx="8" cy="8" r="6.5" fill="none" stroke="#12a383" stroke-width="1.6"/><path d="M1.5 8h13M8 1.5c-3 3.5-3 9.5 0 13M8 1.5c3 3.5 3 9.5 0 13" fill="none" stroke="#12a383" stroke-width="1.2"/></svg>www.verdantworkwear.com</li>
    </ul>

    <svg class="bands" viewBox="0 0 540 120" preserveAspectRatio="none" aria-hidden="true">
      <polygon points="0,92 380,92 392,80 540,80 540,84 394,84 382,96 0,96" fill="var(--brand-blue)"/>
      <polygon points="0,100 384,100 398,86 540,86 540,120 0,120" fill="var(--brand-green)"/>
      <polygon points="370,48 386,34 540,34 540,80 392,80 380,92 370,92" fill="var(--brand-green)"/>
      <polygon points="0,104 540,104 540,108 0,108" fill="var(--brand-blue)" opacity="0"/>
    </svg>
  </section>

  <section class="card card--back" aria-label="Business card back">
    <div class="back-mark"></div>
    <div class="back-name">Verdant<br>Workwear</div>
  </section>

</main>
</body>
</html>
```